Label and packaging - Lune de Sable

We are after label and pack design for a product called Lune de Sable. This product is a blend of Pinot Gris and Apple Cider.

Lune de Sable:

The packaging needs to accomplish the following: quickly explain what the product is, establish as a premium price product and grab the eye. The package should also reflect the product innovation.

Quickly Explain What the Product Is:

Lune de Sable is a nice name that could lift the image – but no one will have any idea what the product is by the name. Consider that a consumer will be staring at a shelf, then the bottle for maybe two to three seconds before moving on to another bottle. In those three seconds we need to make certain that they understand that the product is a blend of wine and cider. Lune de Sable will not support this on its own.

Suggestion is to use words like Wine, Cider, Orchard, Vine, Apple, Heirloom, Exotic and make it simple. Perhaps a sticker that says “50% Wine/50% Apple Cider” that sits on the neck of every bottle. They need to quickly ‘get it”. Imagery will assist as well. Consider a hybrid 50/50 image of wine grapes and apples to tell the story.

Establish a Premium Price Point:

The label needs to say high quality in the package and the font. Have fun with the shipper – this is where you can have a field day with imagery and fun buzz words – we love the idea of a busy shipper that tells the story with a clean and smart looking bottle.

Target Market(s)

This is a premium product targeted at females of age 25-45.

Industry/Entity Type

Consumer

Colors
ec1f27
9bcb3c

Requirements
Must have
• Label design on a burgundy bottle with a screw cap, see here for bottle shape: http://www.vexlabottles.co.nz/wine/#/?view=thumbs&segments=41&colors=&capacityMin=187&capacityMax=750&heightMin=171&heightMax=334&labelMin=44&labelMax=168&neckMin=0&neckMax=1000

Packaging design on a 12 x 750ml carton. This sort of thing: https://www.brakunstores.com.au/images/photo06.jpg

Nice to have
• We have attached some examples of a concept we quite like but it's not bright enough.

```html
<!DOCTYPE html>
<html lang="en">
<head>
<meta charset="utf-8">
<title>Lune de Sable – Bottle Label</title>
<link rel="stylesheet" href="https://fonts.googleapis.com/css2?family=Marcellus&family=Cutive+Mono&display=swap">
<style>
  :root {
    --backdrop: #e4e4e4;
    --glass-yellow: #fde426;
    --glass-light: #fff27a;
    --glass-deep: #f0c800;
    --label-rim: #f7d500;
    --brand-red: #ec1f27;
    --brand-red-deep: #c8101a;
    --brand-green: #9bcb3c;
    --ink-light: #fbe9b8;
    --shadow: rgba(0, 0, 0, 0.28);
  }
  html, body {
    margin: 0;
    padding: 0;
    width: 1197px;
    height: 1200px;
    overflow: hidden;
    background: var(--backdrop);
  }
  .canvas {
    position: relative;
    width: 1197px;
    height: 1200px;
  }
  .bottle {
    position: absolute;
    inset: 0;
  }
  .capsule-name {
    position: absolute;
    left: 588px;
    top: 168px;
    writing-mode: vertical-rl;
    font-family: "Marcellus", serif;
    font-size: 13px;
    letter-spacing: 0.5px;
    color: var(--ink-light);
  }
  .label-name {
    position: absolute;
    margin: 0;
    text-align: center;
    font-family: "Marcellus", serif;
    font-weight: 400;
    line-height: 1;
  }
  .label-name--first {
    left: 498px;
    width: 200px;
    top: 824px;
    font-size: 36px;
    color: var(--brand-red);
  }
  .label-name--second {
    left: 498px;
    width: 200px;
    top: 890px;
    font-size: 42px;
    color: var(--brand-green);
  }
  .label-blend {
    position: absolute;
    left: 500px;
    top: 942px;
    width: 197px;
    margin: 0;
    text-align: center;
    font-family: "Cutive Mono", monospace;
    font-variant: small-caps;
    font-size: 10px;
    line-height: 12px;
    letter-spacing: 1px;
    color: var(--ink-light);
  }
</style>
</head>
<body>
<main class="canvas">
  <svg class="bottle" width="1197" height="1200" viewBox="0 0 1197 1200" aria-hidden="true">
    <defs>
      <linearGradient id="glass" x1="0" x2="1" y1="0" y2="0">
        <stop offset="0" stop-color="var(--glass-deep)"/>
        <stop offset="0.35" stop-color="var(--glass-yellow)"/>
        <stop offset="0.6" stop-color="var(--glass-light)"/>
        <stop offset="1" stop-color="var(--glass-deep)"/>
      </linearGradient>
      <linearGradient id="capsule" x1="0" x2="1" y1="0" y2="0">
        <stop offset="0" stop-color="var(--brand-red-deep)"/>
        <stop offset="0.4" stop-color="var(--brand-red)"/>
        <stop offset="0.7" stop-color="var(--brand-red)"/>
        <stop offset="1" stop-color="var(--brand-red-deep)"/>
      </linearGradient>
      <radialGradient id="floor-shadow">
        <stop offset="0" stop-color="var(--shadow)"/>
        <stop offset="1" stop-color="rgba(0,0,0,0)"/>
      </radialGradient>
    </defs>
    <ellipse class="bottle-shadow" cx="595" cy="1068" rx="210" ry="10" fill="url(#floor-shadow)"/>
    <path class="bottle-glass" fill="url(#glass)"
          d="M556 330 L634 330 C636 420 656 470 688 540 C712 592 722 622 722 662 L722 1052 Q722 1068 706 1068 L484 1068 Q468 1068 468 1052 L468 662 C468 622 478 592 502 540 C534 470 554 420 556 330 Z"/>
    <path class="bottle-punt" d="M548 1066 Q596 990 644 1066 Z" fill="var(--glass-light)" opacity="0.7"/>
    <rect class="bottle-capsule" x="553" y="103" width="84" height="232" rx="8" fill="url(#capsule)"/>
    <rect class="bottle-capsule-lip" x="551" y="103" width="88" height="30" rx="8" fill="var(--brand-red)"/>

    <circle class="label-halo" cx="598" cy="790" r="94" fill="var(--label-rim)"/>
    <circle class="label-emblem" role="img" aria-label="Apple and wine drop emblem" cx="598" cy="784" r="86" fill="var(--brand-green)"/>
    <path class="label-band-rim" d="M498 806 Q598 944 699 806 L699 958 Q699 970 687 970 L510 970 Q498 970 498 958 Z" fill="var(--label-rim)"/>
    <path class="label-band" d="M500 814 Q598 946 697 814 L697 956 Q697 968 685 968 L512 968 Q500 968 500 956 Z" fill="var(--brand-red)"/>
  </svg>

  <span class="capsule-name">Lune de Sable</span>
  <h1 class="label-name label-name--first">Lune</h1>
  <p class="label-name label-name--second">de Sable</p>
  <p class="label-blend">Blend of New Zeland Pinot Gris<br>and Sparkling Apple Cider</p>
</main>
</body>
</html>
```